MEDITERRANEAN Cafe Website needed

We are a MEDITERRANEAN Café serving Coffee, breakfast, Pizza, Pasta, Sandwiches etc.

We need a home page, menu & venue, Reservations & Events, Delivery
Connect (Social media / Feedback / Contact us),Join our team
Updates

Can we keep the designs in Mediterranean colours, look, and feel pleasethanks Added Saturday, December 10, 2016

Project Deadline Extended Reason: I have guarantied the payment and upgraded the project. I would like this would to give more time for new designs to come in and a couple of potential designs to show more. Added Sunday, December 11, 2016

Industry/Entity Type

Cafe

Coding

Coded - Design and coding required

Number of Pages Required

5+ page

Requirements
Must have
• MEDITERRANEAN feel, colours, style etc.
• http://www.corvanetta (DOT) co (DOT) uk
Nice to have

```html
<!DOCTYPE html>
<html lang="en">
<head>
<meta charset="utf-8">
<title>Solara Wraps &amp; Grill</title>
<link rel="stylesheet" href="https://fonts.googleapis.com/css2?family=Josefin+Sans:wght@300;400;600;700&family=Dancing+Script:wght@700&display=swap">
<style>
:root{
  --parchment:#efe0c5;
  --parchment-dark:#e2cca6;
  --ink:#3d3833;
  --teal:#1f5f5f;
  --red:#c0121b;
  --white:#ffffff;
  --rule:#6d655c;
}
*{box-sizing:border-box;margin:0;padding:0}
html,body{width:692px;height:1200px;overflow:hidden}
body{
  position:relative;
  font-family:"Josefin Sans",sans-serif;
  color:var(--ink);
  background:radial-gradient(ellipse at 50% 40%,#f4e8d2 0%,var(--parchment) 55%,var(--parchment-dark) 100%);
}
.site-header{position:absolute;top:0;left:0;width:692px;height:46px;background:#f2e8da;border-bottom:1px solid #d9cbb5}
.brand{position:absolute;left:111px;top:16px;display:flex;align-items:center;gap:4px;white-space:nowrap}
.brand-mark{width:8px;height:8px;border-radius:50%;background:var(--red)}
.brand-name{font-weight:700;font-size:13px;line-height:1;color:var(--red);padding-top:2px}
.main-nav{position:absolute;left:0;top:20px;width:692px;font-size:6.6px;font-weight:600;line-height:1}
.main-nav a{position:absolute;top:0;white-space:nowrap;color:var(--teal);text-decoration:none}
.main-nav a.current{color:#e03b3b}
.book-btn{position:absolute;left:500px;top:14px;width:80px;height:18px;background:var(--red);color:var(--white);font-size:8.5px;font-weight:600;white-space:nowrap;display:flex;align-items:center;justify-content:center;padding-top:2px}
.hero{position:absolute;top:46px;left:0;width:692px;height:226px;overflow:hidden}
.hero-photo{position:absolute;inset:0;background:linear-gradient(90deg,#c4687d 0%,#8fa0a3 28%,#6f6a5a 45%,#5b4030 62%,#a07a55 80%,#e6d6c0 100%)}
.hero-copy{position:absolute;left:108px;top:60px;color:var(--white);text-align:center;width:184px}
.hero-script{font-family:"Dancing Script",cursive;font-size:34px;line-height:1}
.hero-offer{display:flex;align-items:center;justify-content:center;gap:7px;margin-top:2px}
.hero-percent{font-weight:700;font-size:56px;line-height:1}
.hero-off{font-weight:700;font-size:26px;line-height:.85;text-align:left}
.hero-off small{display:block;font-size:19px}
.offer-btn{position:absolute;left:156px;top:160px;width:97px;height:28px;background:var(--red);color:var(--white);font-weight:600;font-size:12px;white-space:nowrap;display:flex;align-items:center;justify-content:center;gap:6px;padding-top:2px}
.menu-cards{position:absolute;top:310px;left:0;width:692px}
.menu-card{position:absolute;width:180px;margin-left:-90px;text-align:center}
.menu-card h2{font-weight:300;font-size:21px;line-height:24px;letter-spacing:.3px}
.menu-card p{font-weight:300;font-size:13px;line-height:17px}
.outline-btn{position:absolute;top:61px;left:45px;width:89px;height:22px;border:1px solid var(--ink);font-size:8px;font-weight:600;white-space:nowrap;display:flex;align-items:center;justify-content:center;gap:5px;padding-top:1px}
.feature{position:absolute;left:111px;top:435px;width:470px;height:186px;background:#5a3d2c;overflow:hidden}
.feature-photo{position:absolute;left:0;top:0;width:235px;height:186px;background:linear-gradient(90deg,#d8b89a 0%,#caa585 60%,#5a3d2c 100%)}
.feature-copy{position:absolute;left:96px;top:30px;color:var(--white);font-weight:300;white-space:nowrap}
.feature-copy .l1{font-size:12px}
.feature-copy .l2{font-size:20px;margin-top:2px}
.feature-copy .l2 em{font-family:"Dancing Script",cursive;font-style:normal;font-size:34px;font-weight:700}
.feature-copy .l3{font-size:10px;margin-top:4px}
.feature-copy .l4{font-size:14px;margin-top:1px}
.red-btn{position:absolute;left:186px;top:138px;width:98px;height:19px;background:var(--red);color:var(--white);font-size:7px;font-weight:600;white-space:nowrap;display:flex;align-items:center;justify-content:center;gap:5px;padding-top:1px}
.video{position:absolute;left:111px;top:646px;width:470px;height:272px;background:radial-gradient(ellipse at 50% 45%,#6b5a48 0%,#453a30 55%,#2e2822 100%)}
.play{position:absolute;left:222px;top:123px;width:26px;height:26px;border-radius:50%;background:var(--white)}
.controls{position:absolute;left:0;bottom:0;width:470px;height:12px;background:#222}
.track{position:absolute;left:14px;top:5px;width:400px;height:3px;background:#666}
.track span{display:block;width:74%;height:3px;background:#ccc}
.time{position:absolute;left:420px;top:2px;font-size:5px;color:#ccc}
.social{position:absolute;top:975px;left:0;width:692px;text-align:center;font-size:17px;font-weight:400}
.social em{font-family:"Dancing Script",cursive;font-style:normal;font-size:26px}
.social-icons{position:absolute;top:1019px;left:274px;display:flex;gap:9px}
.social-icons span{width:30px;height:30px;border-radius:50%;border:1.5px solid var(--ink)}
.footer-rule{position:absolute;top:1064px;left:200px;width:293px;border-top:1px solid var(--rule)}
.footer-nav{position:absolute;top:1083px;left:0;width:692px;font-size:6.5px;font-weight:600}
.footer-nav a{position:absolute;width:80px;margin-left:-40px;text-align:center;white-space:nowrap;color:var(--ink);text-decoration:none}
</style>
</head>
<body>
<header class="site-header">
  <div class="brand"><span class="brand-mark"></span><span class="brand-name">Solara</span></div>
  <nav class="main-nav">
    <a class="current" style="left:175px">HOME</a>
    <a style="left:204px">ABOUT US</a>
    <a style="left:246px">OUR STORY</a>
    <a style="left:291px">OUR MENU</a>
    <a style="left:336px">EVENTS</a>
    <a style="left:370px">CAREERS</a>
    <a style="left:406px">LOCATION</a>
    <a style="left:449px">CONTACT US</a>
  </nav>
  <div class="book-btn">BOOK A TABLE</div>
</header>

<section class="hero">
  <div class="hero-photo" role="img" aria-label="Grilled chicken with rice, salad and red dip on festive bokeh background"></div>
  <div class="hero-copy">
    <div class="hero-script">Festive treats</div>
    <div class="hero-offer"><span class="hero-percent">40%</span><span class="hero-off">OFF<small>MAINS</small></span></div>
  </div>
  <div class="offer-btn">GET OFFER <svg width="7" height="9" viewBox="0 0 7 9"><path d="M1 1l4 3.5L1 8" stroke="#fff" stroke-width="1.8" fill="none"/></svg></div>
</section>

<section class="menu-cards">
  <div class="menu-card" style="left:172px"><h2>BREAKFAST</h2><p>FROM £4.75</p><div class="outline-btn">VIEW MENU <svg width="5" height="7" viewBox="0 0 5 7"><path d="M1 1l2.5 2.5L1 6" stroke="#3d3833" stroke-width="1.3" fill="none"/></svg></div></div>
  <div class="menu-card" style="left:345px"><h2>LUNCH</h2><p>FROM £6.95</p><div class="outline-btn">VIEW MENU <svg width="5" height="7" viewBox="0 0 5 7"><path d="M1 1l2.5 2.5L1 6" stroke="#3d3833" stroke-width="1.3" fill="none"/></svg></div></div>
  <div class="menu-card" style="left:518px"><h2>MAIN MENU</h2><p>ENJOY THE TASTE<br>OF SOLARA</p><div class="outline-btn">VIEW MENU <svg width="5" height="7" viewBox="0 0 5 7"><path d="M1 1l2.5 2.5L1 6" stroke="#3d3833" stroke-width="1.3" fill="none"/></svg></div></div>
</section>

<section class="feature">
  <div class="feature-photo" role="img" aria-label="Bowl of hummus with chickpeas and paprika"></div>
  <div class="feature-copy">
    <div class="l1">CUM SOCIIS NATOQUE PENATIBUS ET MAGNIS</div>
    <div class="l2"><em>Spirit</em> OF MEDITERRANEAN</div>
    <div class="l3">DONEC PRETIUM LIBERO VELIT PRETIUM PORTA NULLA CONGUE</div>
    <div class="l4">PRAESENT LAOREET LIBERO PARTURIENT</div>
  </div>
  <div class="red-btn">VIEW OUR NEW MENU <svg width="5" height="7" viewBox="0 0 5 7"><path d="M1 1l2.5 2.5L1 6" stroke="#fff" stroke-width="1.3" fill="none"/></svg></div>
</section>

<section class="video" role="img" aria-label="Video of a pasta dish with grilled chicken and parsley">
  <div class="play"><svg width="26" height="26" viewBox="0 0 26 26"><path d="M10 8l8 5-8 5z" fill="#3d3833"/></svg></div>
  <div class="controls"><div class="track"><span></span></div><div class="time">0:20</div></div>
</section>

<div class="social">LIKE US, <em>Love us</em>, SHARE US.</div>
<div class="social-icons"><span></span><span></span><span></span><span></span></div>
<div class="footer-rule"></div>
<nav class="footer-nav">
  <a style="left:262px;top:0">HOME</a><a style="left:347px;top:0">OUR MENU</a><a style="left:429px;top:0">LOCATION</a>
  <a style="left:262px;top:19px">ABOUT US</a><a style="left:347px;top:19px">EVENTS</a><a style="left:429px;top:19px">CONTACT US</a>
  <a style="left:262px;top:39px">OUR STORY</a><a style="left:347px;top:39px">CAREERS</a>
</nav>
</body>
</html>
```